Wordpress Theme Design for Glacio-Blaze

Hi, I am looking for an awesome WORDPRESS theme for my snoball and coffee business that is called Glacio-Blaze. This has to be a wordpress theme, because I have other plugins that I would like to use with this site. I want the design to be professional and sophisticated, but also appeal to kids, because after all, the main focus of the business is going to be snoballs, which kids love. I don't want it to look too much like a kiddy site, though. I am also going to be selling other items such as frito pies, hotdogs, cotton candy, nachos, pickles, candy, toys, etc, but the main focus will be the hot and cold aspect of the coffee and snoballs (hence the name, "Glacio-Blaze"). I want the design to look very creative/original and really be attractive to kids, but also very professional so that even adults like coming to the site.
Somewhere in the design I would like to be able to advertise other local businesses in the future, so I would like space incorporated into the design for that. I would also like to be able to add other pages if I want, so there should be space along the top for links, such as "home", "contact", etc. It would also be nice to have a footer in the design for links or other plugins. If you take a look at the site http://quirkypuppyclipsz.example/, I like the functionality of the site (for example, the layout, links, footer, sidebar on other pages), but obviously there isn't much custom design with the theme.
I actually already have a logo designed that I would like incorporated into the look and feel of the design, so that should give you a good place to start with your design. I want the graphics in the theme to really be eye-catching. You are more than welcome to tweak my current logo, blend it into the theme, whatever...(if you want half of the page to be frozen, and the other half to be fire-ish, doesn't have to be, just giving ideas...any and all designs I will take into consideration). Basically, whatever you think would look amazing.
The more amazing the design, I would definitely give a bonus for.
If this helps you out, I'm not looking for a "glossy" style of wordpress design. I really like how this site (CraftHerdly) is made. It uses softer, cleaner colors and designs...it's kind of like a "grunge" style with its text and designs (what I mean is it's not a cookie cutter type of design), but nothing too extreme grunge by any means. I'm looking for the same style as the CraftHerdly site, only with the flare of my type of business.
Hope this helps
Thank you
Reason: The designs, although nice, are not really what I am looking for. These all just feel like they are ready made templates, and I'm looking for something a little more original and unique.

```html
<!DOCTYPE html>
<html lang="en">
<head>
<meta charset="utf-8">
<title>Glacio-Blaze — Snoballs and Coffee</title>
<link rel="stylesheet" href="https://fonts.googleapis.com/css2?family=PT+Sans:wght@400;700&family=PT+Sans+Narrow:wght@400;700&display=swap">
<style>
  :root {
    --sky: #6cc3ef;
    --sky-deep: #4fb3e6;
    --fire: #e0002a;
    --ink: #111111;
    --roast: #2b1d17;
    --beans: #2e2e2e;
    --snow-1: #f4f4f4;
    --snow-2: #e2e3e5;
    --field: #d4d5d6;
    --white: #ffffff;
  }
  * { box-sizing: border-box; margin: 0; padding: 0; }
  html, body { width: 1152px; height: 1200px; overflow: hidden; }
  body { position: relative; background: var(--sky); font-family: "PT Sans Narrow", "Arial Narrow", sans-serif; color: var(--ink); }

  .top-strip { position: absolute; left: 0; top: 0; width: 1152px; height: 8px; background: var(--sky); }
  .bean-backdrop { position: absolute; left: 0; top: 8px; width: 1152px; height: 875px;
    background: radial-gradient(circle at 30% 40%, #3a3a3a, var(--beans) 70%); }

  .site-frame { position: absolute; left: 165px; top: 35px; width: 845px; height: 827px;
    border: 3px solid var(--sky-deep);
    background: linear-gradient(160deg, var(--snow-1), var(--snow-2) 60%, var(--snow-1)); }

  .brand-mark { position: absolute; left: 215px; top: 60px; width: 150px; height: 150px; border-radius: 50%; background: var(--sky); }
  .brand-name { position: absolute; left: 425px; top: 52px; font-weight: 700; font-size: 62px; line-height: 70px; color: var(--roast); letter-spacing: -1px; }

  .social { position: absolute; top: 72px; list-style: none; display: flex; gap: 14px; left: 760px; }
  .social li { font-weight: 700; font-size: 17px; color: var(--roast); width: 62px; text-align: center; line-height: 36px; }

  .tagline { position: absolute; left: 469px; top: 150px; font-family: "PT Sans", sans-serif; font-weight: 700; font-size: 26px; letter-spacing: 11px; white-space: nowrap; }
  .tagline .cold { color: var(--sky); }
  .tagline .and { color: var(--ink); letter-spacing: 8px; margin: 0 10px; }
  .tagline .hot { color: var(--fire); }

  .main-nav { position: absolute; left: 0; top: 210px; width: 1152px; height: 39px; }
  .main-nav a { position: absolute; top: 0; height: 39px; background: var(--sky); border-radius: 5px 5px 0 0;
    font-weight: 700; font-size: 28px; line-height: 40px; text-align: center; color: var(--ink); text-decoration: none; }
  .main-nav a.current { background: var(--fire); }
  .nav-rule { position: absolute; left: 181px; top: 249px; width: 812px; height: 4px; background: var(--fire); }

  .content { position: absolute; left: 181px; top: 253px; width: 812px; height: 589px; background: var(--white); padding: 6px 0 0 30px; }
  .content h1 { font-weight: 700; font-size: 52px; line-height: 60px; }
  .content h2 { font-weight: 700; font-size: 36px; line-height: 38px; color: var(--sky); }
  .content h3 { font-weight: 700; font-size: 24px; line-height: 40px; color: var(--fire); }
  .content p { font-weight: 700; font-size: 22px; line-height: 51px; width: 745px; margin-top: -8px; }

  .footer-widgets { position: absolute; left: 171px; top: 918px; display: flex; }
  .widget { width: 214px; }
  .widget h4 { font-family: "PT Sans", sans-serif; font-weight: 400; font-size: 18px; line-height: 26px; color: var(--ink); margin-bottom: 7px; }
  .widget p { font-family: "PT Sans", sans-serif; font-size: 9.5px; line-height: 12px; color: var(--ink); width: 195px; margin-bottom: 15px; }

  .signup { position: absolute; left: 811px; top: 930px; width: 196px; }
  .signup h4 { font-weight: 700; font-size: 42px; line-height: 38px; color: var(--fire); }
  .signup .field { margin-top: 30px; height: 33px; border-radius: 6px; background: var(--field); border: 2px solid #c4c5c6; }
  .signup .send { margin-top: 13px; height: 41px; border-radius: 6px; background: var(--fire); box-shadow: 0 2px 3px rgba(0,0,0,.25); }
</style>
</head>
<body>
  <div class="top-strip"></div>
  <div class="bean-backdrop" role="img" aria-label="Background of dark roasted coffee beans"></div>

  <div class="site-frame" role="img" aria-label="Light snowy texture behind the header"></div>

  <header>
    <div class="brand-mark"></div>
    <div class="brand-name">Glacio-Blaze</div>
    <ul class="social">
      <li>Linkloop</li>
      <li>Chirper</li>
      <li>Circlely</li>
    </ul>
    <div class="tagline"><span class="cold">SNOBALLS</span><span class="and">and</span><span class="hot">COFFEE</span></div>
    <nav class="main-nav">
      <a class="current" href="#" style="left:432px;width:103px">HOME</a>
      <a href="#" style="left:543px;width:110px">ABOUT</a>
      <a href="#" style="left:661px;width:137px">CONTACT</a>
      <a href="#" style="left:804px;width:82px">FAQ</a>
      <a href="#" style="left:892px;width:101px">MENU</a>
    </nav>
    <div class="nav-rule"></div>
  </header>

  <main class="content">
    <h1>Main Page Content</h1>
    <h2>Include Information About Product</h2>
    <h3>Depending on what you need</h3>
    <p>Lorem ipsum dolor sit amet, consectetur adipiscing elit. Phasellus consectetur tortor id odio feugiat consequat. Phasellus vehicula, odio in euismod pulvinar, augue mi vulputate nisi, ac consequat libero lectus vitae massa. Donec interdum, augue a pharetra dignissim, nisl velit vehicula tortor, ac rhoncus tellus ante id nibh. Etiam aliquam euismod ultrices. In eu mi sem, in tempus metus. Aenean sed dolor sem, sit amet imperdiet urna. Duis accumsan purus quis tellus mattis elementum. Proin urna lacus, gravida vel molestie et, gravida a risus. In a tempus dolor. Cum sociis natoque penatibus et magnis dis parturient montes, nascetur ridiculus mus.</p>
  </main>

  <footer>
    <div class="footer-widgets">
      <section class="widget">
        <h4>Widgets</h4>
        <p>Lorem ipsum dolor sit amet, consectetur adipiscing elit. In suscipit ante sit amet neque</p>
        <p>Lorem ipsum dolor sit amet, consectetur adipiscing elit. In suscipit ante sit amet neque</p>
        <p>Lorem ipsum dolor sit amet, consectetur adipiscing elit. In suscipit ante sit amet neque</p>
        <p>Lorem ipsum dolor sit amet, consectetur adipiscing elit. In suscipit ante sit amet neque</p>
        <p>Lorem ipsum dolor sit amet, consectetur adipiscing elit. In suscipit ante sit amet neque</p>
      </section>
      <section class="widget">
        <h4>Widgets</h4>
        <p>Lorem ipsum dolor sit amet, consectetur adipiscing elit. In suscipit ante sit amet neque</p>
        <p>Lorem ipsum dolor sit amet, consectetur adipiscing elit. In suscipit ante sit amet neque</p>
        <p>Lorem ipsum dolor sit amet, consectetur adipiscing elit. In suscipit ante sit amet neque</p>
        <p>Lorem ipsum dolor sit amet, consectetur adipiscing elit. In suscipit ante sit amet neque</p>
        <p>Lorem ipsum dolor sit amet, consectetur adipiscing elit. In suscipit ante sit amet neque</p>
      </section>
      <section class="widget">
        <h4>Widgets</h4>
        <p>Lorem ipsum dolor sit amet, consectetur adipiscing elit. In suscipit ante sit amet neque</p>
        <p>Lorem ipsum dolor sit amet, consectetur adipiscing elit. In suscipit ante sit amet neque</p>
        <p>Lorem ipsum dolor sit amet, consectetur adipiscing elit. In suscipit ante sit amet neque</p>
        <p>Lorem ipsum dolor sit amet, consectetur adipiscing elit. In suscipit ante sit amet neque</p>
        <p>Lorem ipsum dolor sit amet, consectetur adipiscing elit. In suscipit ante sit amet neque</p>
      </section>
    </div>
    <div class="signup">
      <h4>Sign-Up for Updates</h4>
      <div class="field"></div>
      <div class="send"></div>
    </div>
  </footer>
</body>
</html>
```